Torvenu Business Card Design Project

We need a business card design for torvenu.com a company based in Berlin, Germany.

?Torvenu is marketplace that enables people all over the world to monetize and exchange their individual knowledge and language skills through interactive video sessions. User are matched by their interests.

On Torvenu everybody can be student or teacher (seller or buyer).

We would love to see designs that use or main color blue and green. The design should communicate what Torvenu enables - see my notice above.

Looking so forward to your designs
Cheers from Berlin,
Konrad

Target Market(s)

globally

Industry/Entity Type

Teacher

Requirements
Must have
• Konrad Wielert
CEO
Torvenu.com

Torvenu e-Services GmbH
Lindgrubweg 27
10117 Berlin

Fon: +49 30 481 906 27 14
Mobile: 49 171 57 04 91 3
E-Mail: k.wielert@torvenu.com
Web: www.torvenu.com

```html
<!DOCTYPE html>
<html lang="en">
<head>
<meta charset="utf-8">
<title>Torvenu Business Card</title>
<link rel="stylesheet" href="https://fonts.googleapis.com/css2?family=Jost:wght@400;500;600&display=swap">
<style>
  :root {
    --stage: #6b6a69;
    --blue-light: #27a0dc;
    --blue-deep: #3a5aa6;
    --blue-text: #2aa2dd;
    --green: #95c11f;
    --ink: #5d5d5d;
    --paper: #f3f3f3;
    --paper-edge: #e9e9e6;
    --front-word: #ececec;
  }
  * { margin: 0; padding: 0; box-sizing: border-box; }
  html, body {
    width: 1200px; height: 486px; overflow: hidden;
    background: var(--stage);
    font-family: "Jost", "Century Gothic", sans-serif;
  }
  .stage { position: relative; width: 1200px; height: 486px; }

  .card {
    position: absolute; top: 116px;
    width: 517px; height: 299px; overflow: hidden;
  }
  .lockup-mark { position: absolute; background: var(--green); }
  .wordmark { position: absolute; font-weight: 400; line-height: 1; white-space: nowrap; }
  .tagline { position: absolute; line-height: 1; white-space: nowrap; color: var(--blue-text); }

  /* Front */
  .card--front {
    left: 87px;
    background: radial-gradient(ellipse 70% 60% at 50% 10%, var(--blue-light) 0%, #2b7fcc 50%, var(--blue-deep) 100%);
  }
  .front-wash { position: absolute; inset: 0; }
  .card--front .lockup-mark { left: 62px; top: 110px; width: 74px; height: 74px; }
  .card--front .wordmark {
    left: 150px; top: 88px; font-size: 84px; letter-spacing: 1.5px; color: var(--front-word);
  }
  .card--front .tagline {
    left: 181px; top: 170px; font-size: 17px; letter-spacing: 5.2px;
  }

  /* Back */
  .card--back {
    left: 630px;
    background: linear-gradient(180deg, #f7f7f7 0%, var(--paper) 60%, var(--paper-edge) 100%);
  }
  .card--back .lockup-mark { left: 33px; top: 39px; width: 57px; height: 57px; }
  .card--back .wordmark {
    left: 100px; top: 28px; font-size: 64px; letter-spacing: 1px; color: var(--ink);
  }
  .card--back .tagline {
    left: 123px; top: 84px; font-size: 13px; letter-spacing: 4px;
  }

  .person { position: absolute; left: 36px; top: 131px; }
  .person__name { font-size: 18px; font-weight: 600; color: var(--ink); line-height: 24px; }
  .person__role { font-size: 19px; color: var(--blue-text); line-height: 22px; }

  .contact { position: absolute; left: 33px; top: 184px; list-style: none; }
  .contact li {
    display: flex; align-items: center; gap: 11px;
    font-size: 19px; color: var(--ink); height: 22.5px; white-space: nowrap;
  }
  .contact svg { width: 16px; height: 16px; fill: var(--ink); flex: none; }

  .address {
    position: absolute; left: 292px; top: 187px;
    font-size: 19px; line-height: 22.5px; color: var(--ink); font-style: normal; white-space: nowrap;
  }
  .web-band {
    position: absolute; left: 0; bottom: 0; width: 100%; height: 34px;
    background: linear-gradient(90deg, #3e6aaf, var(--blue-deep));
    display: flex; align-items: center; justify-content: center;
    font-size: 16px; font-weight: 600; color: var(--blue-text);
  }
</style>
</head>
<body>
<main class="stage">
  <section class="card card--front" aria-label="Business card front">
    <div class="front-wash" role="img" aria-label="Soft blue background with a faint repeating brand pattern"></div>
    <span class="lockup-mark"></span>
    <span class="wordmark">torvenu</span>
    <p class="tagline">share what you know</p>
  </section>

  <section class="card card--back" aria-label="Business card back">
    <span class="lockup-mark"></span>
    <span class="wordmark">torvenu</span>
    <p class="tagline">share what you know</p>

    <div class="person">
      <p class="person__name">Konrad Wielert</p>
      <p class="person__role">CEO</p>
    </div>

    <ul class="contact">
      <li>
        <svg viewBox="0 0 16 16" aria-hidden="true"><path d="M1 5c0-2 3-3 7-3s7 1 7 3v1h-3V5H4v1H1z"/><path d="M3 7h10l1 7H2z"/></svg>
        +49 30 481 906 27 14
      </li>
      <li>
        <svg viewBox="0 0 16 16" aria-hidden="true"><path d="M4 1h8v14H4zM5.5 3v4h5V3zM5.5 9h1.5v1.5H5.5zm3 0H10v1.5H8.5zm-3 2.5h1.5V13H5.5zm3 0H10V13H8.5z"/></svg>
        49 171 57 04 91 3
      </li>
      <li>
        <svg viewBox="0 0 16 16" aria-hidden="true"><path d="M1 3h14v10H1zm1.5 1.5v.3L8 9l5.5-4.2v-.3zM2.5 6.7v4.8h11V6.7L8 11z"/></svg>
        k.wielert@torvenu.com
      </li>
    </ul>

    <address class="address">
      Torvenu e-Services GmbH<br>
      Lindgrubweg 27<br>
      10117 Berlin
    </address>

    <div class="web-band">Torvenu.com</div>
  </section>
</main>
</body>
</html>
```